Smart Home App Needs 4 Mockup Screens. Extra Work Guaranteed for Winner

BACKGROUND
Our company, Lumora, is launching an exciting new app early next year. And we need some examples of what our app will look like to show to some of the biggest retailers in the world. We hope that this project will lead to regular work as we have a lot of new products planned for the app.

Our app will support baby, home and pet monitors (cameras) as well as the world's first smart pet flap.

The monitors allow you to do much more than just watch live video. By monitoring and providing information on sound, movement and temperature the app provides the user with instant peace of mind wherever they are. If anything has changed the user can be alerted via notifications. If motion is detected the user will receive a clip of the whole event moments after it has happened.

The Smart Pet Flap is packed full of features too. From letting you decide when your pet can or can't go outside from your mobile, to automatically opening if a fire is detected (along with a whole host of other features) - this really is the most advanced pet flap in the world.

REQUIREMENTS
We need 4 mock-up screens creating to show the UI of our app.
1. Camera Home Page
2. Camera Notifications Page
3. Pet Flap Fire Alarm Warning Page
4. Extreme Weather Warning Page

Optional - Happy to Pay the Winner Extra for these Designs
5. Start Up/Log In Page
6. Pet Flap Notification Example
7. Pet Flap Scheduler Page (your choice)
(SEE LUMORA APP DESIGN COMPETITION - ATTACHED)

STYLE GUIDE
As you'll see from our wireframes we want our app to be very minimal and modern. The predominant colour will be white but where colour is used it should be bright (see our colour palette - which we will provide shortly).

INSPIRATION
We love the UI of Finchly (home surveillance). Also check out Vesk (smart thermostat).
(SEE LUMORA UI EXAMPLES ATTACHED)

LOGO
We love our logo. Feel free to use it in creative ways.

So far we're also using it as a kind of beacon to indicate if everything is ok.

LOGO COLOURS & APP COLOURS
As mentioned, we are thinking of using the green logo to indicate that everything is ok (and also for the pet app in general). We reserve red for when something has happened (normally bad) and needs attention, like a fire alarm going off.

The app will be predominantly black and white with the odd minimal flash of colour (probably primary colour)
We'll upload a colour scheme as soon as we have it.

CONTACT
Please message us for more details - we'll do our best to reply promptly.

FUTURE WORK
We will need extra screens made straight after the competition is over and there should be additional regular work after this.

Target Market(s)

Our app will be used by young professionals, to young parents to grandparents. The design must be contemporary but timeless and easy to use no matter how good you are with technology.

Industry/Entity Type

Pet

Font styles to use
Sans Serif

Colors
faee3f
33a6d7
ec1f27
acd036
32b7a4

Requirements
Must have
• Beautiful, minimal design. Make sure you spend time looking at the Finchly and Vesk apps before starting.

For the videos make sure you use sensible images - that you'd expect to see from a monitor (high resolution images if possible)
Nice to have
• Creative use of our logo.
Should not have
• Too much detail/clutter/colours. Ugly fonts.

```html
<!DOCTYPE html>
<html lang="en">
<head>
<meta charset="utf-8">
<title>Lumora – Pet Flap Fire Alarm Warning</title>
<link rel="stylesheet" href="https://fonts.googleapis.com/css2?family=Arimo:wght@400;700&display=swap">
<style>
  :root {
    --screen-bg: #f2f2f2;
    --hero-bg: #dcdcdc;
    --alert-red: #e8432c;
    --heading-ink: #333333;
    --action-green: #5cb84a;
    --button-text: #ffffff;
    --flame-yellow: #f7c52e;
    --flame-orange: #f08a24;
  }
  * { box-sizing: border-box; margin: 0; padding: 0; }
  html, body {
    width: 1200px;
    height: 2481px;
    overflow: hidden;
  }
  body {
    background: var(--screen-bg);
    font-family: "Arimo", Helvetica, Arial, sans-serif;
    position: relative;
  }
  .alert-hero {
    position: absolute;
    left: 0; top: 0;
    width: 1200px;
    height: 799px;
    background: var(--hero-bg);
  }
  .alert-hero__artwork {
    position: absolute;
    left: 401px;
    top: 75px;
    width: 405px;
    height: 611px;
    border-radius: 40px;
    background: linear-gradient(180deg, var(--flame-yellow) 0%, var(--flame-orange) 45%, var(--alert-red) 100%);
  }
  .alert-message {
    position: absolute;
    left: 52px;
    top: 868px;
    width: 1100px;
    color: var(--alert-red);
    font-size: 64px;
    line-height: 94px;
    font-weight: 400;
  }
  .choice-heading {
    position: absolute;
    left: 0;
    top: 1196px;
    width: 1200px;
    text-align: center;
    color: var(--heading-ink);
    font-size: 88px;
    font-weight: 700;
    line-height: 106px;
  }
  .choice-list {
    position: absolute;
    left: 68px;
    top: 1388px;
    width: 1061px;
    list-style: none;
  }
  .choice-button {
    display: flex;
    align-items: center;
    justify-content: center;
    height: 180px;
    margin-bottom: 63px;
    padding: 0 60px;
    border-radius: 11px;
    background: var(--action-green);
    color: var(--button-text);
    font-size: 64px;
    line-height: 70px;
    text-align: center;
  }
</style>
</head>
<body>
  <header class="alert-hero">
    <div class="alert-hero__artwork" role="img" aria-label="Warning triangle with exclamation mark engulfed in flames"></div>
  </header>

  <p class="alert-message">Your fire alarm is going off. Rex is already outside so we have locked him out as a precaution.</p>

  <h1 class="choice-heading">What do you want to do?</h1>

  <ul class="choice-list">
    <li class="choice-button">Keep him locked out untill further notice</li>
    <li class="choice-button">It’s a false alarm - let him back in</li>
    <li class="choice-button">Make a call</li>
  </ul>
</body>
</html>
```